Marrowgate Pictures Pty needs poster design for Australian feature film thriller

In the tradition of great classic “serial killer” films such as Velvet Tenant and Harbinger, the thriller "Quiet Stranger" promises mystery, excitement and, of course, the ultimate battle between good and evil. A modern city is hit with a string of continuing inexplicable murders of seemingly random women from different cultural and socio-economic backgrounds. The audience journeys with the murderer as he carries out his deadly deeds. We also follow the dedicated police force which will not let go of every possible lead. What happens when the murderer meets the last standing policewoman on his trail will leave audiences in shock!

We are looking for a poster design for this film which is a tribute to Howard Keswick's film "Shadow at Nine." Poster should be classy and grabs the viewer emotionally.

The film "Quiet Stranger" is in post-production. The film will be sent to international film festivals. I've uploaded the following:
1. some posters I like (please be creative in your own style)
2. a credit list that needs to be on the poster
3. photos of "The quiet Stranger" facing different directions and in different emotions
4. some of his female victims for your reference and inspiration
5. some on-set photos of Quiet Stranger with some of his potential victims for your reference and inspiration

Target Market(s)

International Western audiences who love thrillers

Requirements
Must have
• Something that grabs the emotions and intrigues the viewer to come see the film
Nice to have
• n/a
Should not have
• n/a

```html
<!DOCTYPE html>
<html lang="en">
<head>
<meta charset="utf-8">
<title>Quiet Stranger — Poster</title>
<link href="https://fonts.googleapis.com/css2?family=Cinzel:wght@400;500&family=Oswald:wght@400;500&display=swap" rel="stylesheet">
<style>
  :root {
    --paper: #ffffff;
    --blood: #f0201a;
    --ink: #1a1110;
    --white: #ffffff;
    --suit-dark: #1c1c1c;
    --suit-mid: #4a4a4a;
    --streak: #2a0d0b;
  }
  * { margin: 0; padding: 0; box-sizing: border-box; }
  html, body { width: 823px; height: 1200px; overflow: hidden; background: var(--paper); }
  .poster {
    position: absolute; left: 19px; top: 19px; width: 785px; height: 1162px;
    background: var(--blood); overflow: hidden;
    font-family: "Cinzel", "Times New Roman", serif; color: var(--white);
  }
  .director-credit {
    position: absolute; top: 22px; left: 0; width: 100%; text-align: center;
    font-size: 24px; line-height: 30px; letter-spacing: 3px; font-weight: 400;
  }
  .director-credit .small { font-size: 19px; display: block; line-height: 24px; }
  .director-credit .line { display: block; }
  .hero-figure {
    position: absolute; left: 290px; top: 152px; width: 170px; height: 650px;
    background: linear-gradient(180deg, var(--suit-mid) 0%, var(--suit-dark) 40%, #2e2e2e 100%);
    opacity: .85;
  }
  .cast { position: absolute; left: 283px; width: 230px; }
  .cast-row { display: flex; justify-content: space-between; font-size: 25px; line-height: 30px; }
  .floor-streaks { position: absolute; left: 0; top: 800px; width: 785px; height: 50px; }
  .title {
    position: absolute; left: 0; width: 100%; text-align: center;
    font-weight: 400; line-height: 1; font-family: "Cinzel", "Times New Roman", serif;
  }
  .title-top { top: 870px; color: var(--ink); font-size: 80px; letter-spacing: 12px; }
  .title-bottom { top: 962px; color: var(--white); font-size: 88px; letter-spacing: 8px; }
  .billing {
    position: absolute; left: 0; top: 1083px; width: 100%; text-align: center;
    font-family: "Oswald", "Arial Narrow", sans-serif; font-size: 9.5px; line-height: 13px;
    letter-spacing: .3px; text-transform: uppercase;
  }
  .billing .label { font-size: 5px; display: inline-block; width: 34px; line-height: 5px; vertical-align: middle; text-align: right; margin-right: 2px; }
  .billing .copyright { font-size: 6px; text-transform: none; }
</style>
</head>
<body>
<main class="poster">
  <header class="director-credit">
    <span class="small">A</span>
    <span class="line">REN-MARIE HOLLIS</span>
    <span class="line">FILM</span>
  </header>

  <div class="hero-figure" role="img" aria-label="Man in a dark suit seen in profile, holding a straight razor at his side"></div>

  <section class="cast" style="top:262px"><div class="cast-row"><span>T</span><span>A</span><span>R</span><span>E</span><span>K</span></div><div class="cast-row"><span>S</span><span>O</span><span>L</span><span>A</span><span>N</span><span>K</span><span>I</span></div></section>
  <section class="cast" style="top:342px"><div class="cast-row"><span>M</span><span>A</span><span>T</span><span>E</span><span>O</span></div><div class="cast-row"><span>F</span><span>E</span><span>R</span><span>R</span><span>A</span><span>N</span><span>D</span></div></section>
  <section class="cast" style="top:422px"><div class="cast-row"><span>N</span><span>O</span><span>R</span><span>A</span></div><div class="cast-row"><span>V</span><span>E</span><span>L</span><span>L</span></div></section>
  <section class="cast" style="top:542px"><div class="cast-row"><span>C</span><span>A</span><span>L</span><span>L</span><span>U</span><span>M</span></div><div class="cast-row"><span>B</span><span>R</span><span>I</span><span>S</span><span>K</span></div></section>
  <section class="cast" style="top:622px"><div class="cast-row"><span>O</span><span>W</span><span>E</span><span>N</span></div><div class="cast-row"><span>H</span><span>A</span><span>R</span><span>L</span><span>O</span><span>W</span></div></section>

  <svg class="floor-streaks" viewBox="0 0 785 50" aria-hidden="true">
    <g stroke="var(--streak)" stroke-linecap="round">
      <line x1="0" y1="6" x2="785" y2="5" stroke-width="2" opacity=".7"/>
      <line x1="0" y1="14" x2="785" y2="16" stroke-width="4" opacity=".55"/>
      <line x1="20" y1="23" x2="760" y2="22" stroke-width="1.5" opacity=".6"/>
      <line x1="0" y1="31" x2="785" y2="32" stroke-width="3" opacity=".45"/>
      <line x1="60" y1="40" x2="720" y2="39" stroke-width="1" opacity=".5"/>
    </g>
  </svg>

  <h1 class="title title-top">QUIET</h1>
  <h1 class="title title-bottom">STRANGER</h1>

  <footer class="billing">
    Fenwick Films Pty Ltd &amp; Marrowgate Pictures Pty Ltd present<br>
    A Ren-Marie Hollis film ‘Quiet Stranger’ starring Tarek Solanki, Nora Vell, Mateo Ferrand, Callum Brisk, Owen Harlow<br>
    <span class="label">executive producers</span>Tarek Solanki &amp; Ren-Marie Hollis
    <span class="label">director of photography</span>Reid Calder
    <span class="label">sound design</span>Gus Pendry
    <span class="label">music composer</span>Lyle Basset
    <span class="label">casting</span>Marrowgate Pictures Pty Ltd<br>
    <span class="label">art direction</span>Tessa Moorcroft &amp; Paul Ainsley
    <span class="label">makeup artist</span>Dana Wickham
    <span class="label">costume design</span>Ivy Castell
    <span class="label">original story</span>Tarek Nadira<br>
    <span class="label">screenplay by</span>Nadira Joss &amp; Ren-Marie Hollis
    <span class="label">directed by</span>Ren-Marie Hollis<br>
    <span class="copyright">Copyright © 2016 Fenwick Films Pty Ltd &amp; Marrowgate Pictures Pty Ltd. All rights reserved.</span>
  </footer>
</main>
</body>
</html>
```